Business Card Design Project

A polished, very professional looking business card. I think we want to keep it all grey. I've attached our old logo, and current mockup in which case we really like the font.

Target Market(s)

Target Market are Bride and Grooms and Wedding Coordinators. We are wedding photographers

Industry/Entity Type

Business

Font styles to use
Serif
Sans Serif

Requirements
Must have
• An elegant, yet simple and sophisticated appearance.

Phone number, Email, Website and Social Media link.
Nice to have
• An element that can be spot glossed when printed. Not necessary though.
Should not have
• Bright colors, images or intensive graphics.

```html
<!DOCTYPE html>
<html lang="en">
<head>
<meta charset="utf-8">
<title>Carter Langley Photographers – Business Card</title>
<link rel="stylesheet" href="https://fonts.googleapis.com/css2?family=Cinzel:wght@400;500&family=Roboto+Condensed:wght@300&family=Montserrat:wght@700&display=swap">
<style>
  :root {
    --card-dark: #414143;
    --card-light: #e4e3e4;
    --band-light: #dcdcdc;
    --band-shade: #a9a9a9;
    --ink-white: #ffffff;
    --ink-band: #3f3f41;
    --icon-stroke: #f2f2f2;
  }
  * { margin: 0; padding: 0; box-sizing: border-box; }
  html, body { width: 1200px; height: 741px; overflow: hidden; background: var(--card-dark); }
  .card {
    position: relative;
    width: 1200px;
    height: 741px;
    background: var(--card-dark);
    overflow: hidden;
  }
  .top-strip {
    position: absolute; left: 0; top: 0; width: 100%; height: 16px;
    background: var(--card-light);
  }
  .brand-mark {
    position: absolute; left: 248px; top: 203px; width: 117px; height: 118px;
    background: var(--ink-white);
  }
  .brand-rule {
    position: absolute; left: 279px; top: 355px; width: 51px; height: 2px;
    background: var(--ink-white); border-radius: 50%;
  }
  .brand-name {
    position: absolute; left: 40px; top: 388px; width: 522px;
    text-align: center;
    font-family: "Cinzel", serif; font-weight: 400;
    font-size: 50px; letter-spacing: 5px; line-height: 1;
    color: var(--ink-white);
  }
  .brand-trade {
    position: absolute; left: 40px; top: 458px; width: 522px;
    text-align: center;
    font-family: "Montserrat", sans-serif; font-weight: 700;
    font-size: 16px; letter-spacing: 10.5px; line-height: 1;
    color: var(--ink-white);
  }
  .divider {
    position: absolute; left: 599px; top: 158px; width: 3px; height: 362px;
    background: linear-gradient(to bottom, rgba(255,255,255,0) 0%, #ffffff 50%, rgba(255,255,255,0) 100%);
  }
  .contact-list { position: absolute; left: 655px; top: 208px; list-style: none; }
  .contact-item {
    display: flex; align-items: center; height: 54.5px;
    font-family: "Roboto Condensed", sans-serif; font-weight: 300;
    font-size: 25px; letter-spacing: 0.3px;
    color: var(--ink-white);
  }
  .contact-icon { width: 32px; height: 32px; margin-right: 50px; flex: none; }
  .footer-band {
    position: absolute; left: 0; top: 570px; width: 1200px; height: 134px;
  }
  .tagline {
    position: absolute; left: 0; top: 656px; width: 1200px;
    text-align: center;
    font-family: "Cinzel", serif; font-weight: 500;
    font-size: 25px; letter-spacing: 2px; line-height: 1;
    color: var(--ink-band);
  }
</style>
</head>
<body>
<div class="card">
  <div class="top-strip"></div>

  <div class="brand-mark"></div>
  <div class="brand-rule"></div>
  <div class="brand-name">Carter Langley</div>
  <div class="brand-trade">PHOTOGRAPHERS</div>

  <div class="divider"></div>

  <ul class="contact-list">
    <li class="contact-item">
      <svg class="contact-icon" viewBox="0 0 32 32" fill="none" stroke="var(--icon-stroke)" stroke-width="1.6">
        <circle cx="16" cy="16" r="14"/>
        <rect x="11.5" y="8" width="9" height="16" rx="1.5"/>
        <line x1="11.5" y1="20.5" x2="20.5" y2="20.5"/>
      </svg>
      555.240.7316
    </li>
    <li class="contact-item">
      <svg class="contact-icon" viewBox="0 0 32 32" fill="none" stroke="var(--icon-stroke)" stroke-width="1.6">
        <circle cx="16" cy="16" r="14"/>
      </svg>
      socialpage.com/CarterLangleyPhoto
    </li>
    <li class="contact-item">
      <svg class="contact-icon" viewBox="0 0 32 32" fill="none" stroke="var(--icon-stroke)" stroke-width="1.6">
        <circle cx="16" cy="16" r="14"/>
      </svg>
      chirpline.com/CarterLangley
    </li>
    <li class="contact-item">
      <svg class="contact-icon" viewBox="0 0 32 32" fill="none" stroke="var(--icon-stroke)" stroke-width="1.6">
        <circle cx="16" cy="16" r="14"/>
        <circle cx="16" cy="16" r="4"/>
        <path d="M20 12v5.5a2.5 2.5 0 0 0 5 0V16a9 9 0 1 0-3.5 7.1"/>
      </svg>
      carter@carterlangley.com
    </li>
    <li class="contact-item">
      <svg class="contact-icon" viewBox="0 0 32 32" fill="none" stroke="var(--icon-stroke)" stroke-width="1.6">
        <circle cx="16" cy="16" r="14"/>
        <circle cx="16" cy="16" r="8.5"/>
        <ellipse cx="16" cy="16" rx="3.5" ry="8.5"/>
        <line x1="7.5" y1="16" x2="24.5" y2="16"/>
      </svg>
      www.carterlangley.com
    </li>
  </ul>

  <svg class="footer-band" viewBox="0 0 1200 134" preserveAspectRatio="none">
    <defs>
      <linearGradient id="bandFill" x1="0" y1="0" x2="1" y2="0">
        <stop offset="0" stop-color="#d4d4d4"/>
        <stop offset="0.5" stop-color="#f1f1f1"/>
        <stop offset="0.8" stop-color="#dadada"/>
        <stop offset="1" stop-color="var(--band-shade)"/>
      </linearGradient>
    </defs>
    <path d="M0 66 H818 C850 66 855 2 905 2 H1200 V134 H0 Z" fill="url(#bandFill)"/>
  </svg>
  <div class="tagline">California based wedding and portrait photographer</div>
</div>
</body>
</html>
```